Refresh of graphic design for existing website

We would like to refresh our website. Please see the attached design specifications.

Industry/Entity Type

Graphic Design

```html
<!DOCTYPE html>
<html lang="en">
<head>
<meta charset="utf-8">
<title>Garage Tools Alliance</title>
<link rel="stylesheet" href="https://fonts.googleapis.com/css2?family=Open+Sans:wght@400;600;700;800&display=swap">
<style>
:root{
  --navy:#1d2a5c;
  --navy-deep:#131d45;
  --yellow:#f4c21a;
  --yellow-dark:#d9a900;
  --ink:#222;
  --muted:#555;
  --paper:#ffffff;
  --soft:#f1f1f1;
}
*{box-sizing:border-box;margin:0;padding:0}
html,body{width:739px;height:1200px;overflow:hidden}
body{font-family:"Open Sans",Arial,sans-serif;color:var(--ink);background:var(--paper);position:relative}
a{color:inherit;text-decoration:none}

/* header */
.site-header{position:absolute;top:0;left:0;width:739px;height:74px}
.brand{position:absolute;left:18px;top:0;width:118px;height:68px;background:var(--paper);display:flex;align-items:center;justify-content:center;gap:6px;z-index:3;clip-path:polygon(0 0,100% 0,100% 80%,50% 100%,0 80%)}
.brand-dot{width:12px;height:12px;border-radius:50%;background:var(--navy)}
.brand-name{font-weight:800;font-size:24px;color:var(--navy)}
.top-strip{position:absolute;left:0;top:0;width:739px;height:44px;background:var(--paper);border-bottom:1px solid #ddd}
.tagline-bar{position:absolute;left:136px;top:8px;width:330px;height:22px;background:var(--yellow);font-size:9.5px;font-weight:600;color:var(--navy);line-height:22px;padding-left:12px}
.search{position:absolute;left:492px;top:8px;width:114px;height:22px;background:#fff;border:1px solid #aaa;font-size:8.5px;color:#888;line-height:20px;padding-left:6px}
.socials{position:absolute;left:624px;top:8px;display:flex;gap:7px}
.socials span{width:22px;height:22px;border-radius:50%;background:var(--navy);display:block}
.main-nav{position:absolute;left:0;top:44px;width:739px;height:30px;background:var(--navy)}
.main-nav ul{list-style:none;display:flex;gap:26px;padding-left:150px;height:30px;align-items:center}
.main-nav li{font-size:8.5px;color:#fff;font-weight:600}

/* hero */
.hero{position:absolute;left:0;top:74px;width:739px;height:306px;background:linear-gradient(120deg,#b9c2c9 0%,#e4e7ea 35%,#cfd7e2 55%,#3a5aa8 78%,#2a3e7a 100%)}
.login{position:absolute;left:40px;top:56px;width:150px;height:178px;background:rgba(8,12,30,.92);padding:14px 12px}
.login h2{color:var(--yellow);font-size:13px;font-weight:700;line-height:1.25;text-align:center;margin-bottom:16px}
.field{display:flex;align-items:center;justify-content:space-between;margin-bottom:10px}
.field label{color:var(--yellow);font-size:8.5px;font-weight:600}
.field span{width:82px;height:18px;background:#fff;border-radius:2px}
.login-actions{display:flex;justify-content:space-between;align-items:center;margin-top:18px}
.login-actions a{color:#fff;font-size:7.5px}
.btn-login{background:var(--yellow);color:var(--navy);font-size:8px;font-weight:700;padding:4px 12px;border-radius:3px}
.dots{position:absolute;left:342px;top:276px;display:flex;gap:7px}
.dots span{width:8px;height:8px;border-radius:50%;background:var(--yellow)}
.dots span:first-child{background:#fff}

/* intro */
.intro{position:absolute;left:0;top:380px;width:739px;height:150px;display:flex;padding:30px 30px 0 58px}
.intro-lead{width:190px;font-size:12.5px;font-weight:700;line-height:1.6;color:#333;letter-spacing:.2px;padding-top:4px}
.intro-body{margin-left:28px;border-left:2px solid #333;padding-left:16px;width:420px}
.intro-body h2{font-size:13px;font-weight:800;color:#222;margin-bottom:6px}
.intro-body p{font-size:7.5px;line-height:1.55;color:var(--muted)}

/* events */
.events{position:absolute;left:0;top:530px;width:739px;height:195px;background:var(--soft)}
.events h2{text-align:center;font-size:15px;font-weight:700;color:var(--navy);padding-top:12px}
.events h2::after{content:"";display:block;width:50px;height:2px;background:var(--yellow);margin:4px auto 0}
.event-grid{display:grid;grid-template-columns:1fr 1fr;column-gap:30px;row-gap:16px;padding:16px 50px 0 50px}
.event{display:flex;gap:8px}
.event-icon{flex:none;width:34px;height:34px;border-radius:50%;background:var(--yellow);display:flex;align-items:center;justify-content:center}
.event h3{font-size:9.5px;font-weight:700;color:var(--navy);margin-bottom:3px}
.event p{font-size:7px;line-height:1.45;color:var(--muted)}

/* panels */
.panels{position:absolute;left:0;top:725px;width:739px;height:150px;display:flex;gap:28px;padding:12px 50px 0 50px}
.panel{flex:1;background:var(--navy);border-radius:4px;overflow:hidden}
.panel h2{background:var(--yellow);color:var(--navy);font-size:11px;font-weight:700;text-align:center;height:22px;line-height:22px}
.panel-body{padding:8px 10px;color:#fff;font-size:7px;line-height:1.5}
.news-item{margin-bottom:6px}
.news-item strong{color:var(--yellow);display:block}
.news-item em{font-style:normal;color:#cfd6ee}
.quick-grid{display:grid;grid-template-columns:1fr 1fr;gap:7px 8px;padding:6px 2px}
.quick-grid span{border:1px solid #fff;border-radius:10px;text-align:center;padding:3px 0;font-size:7px}
.quick-grid span.wide{grid-column:1 / 3;width:60px;justify-self:center}
.join strong{color:var(--yellow)}
.btn-join{display:inline-block;margin-top:6px;background:var(--yellow);color:var(--navy);font-weight:700;padding:2px 10px;border-radius:3px}

/* contact */
.contact-row{position:absolute;left:0;top:875px;width:739px;height:60px;display:flex;justify-content:space-around;align-items:center;padding:0 40px;font-size:12px;font-weight:700;color:var(--navy)}
.contact-band{position:absolute;left:0;top:935px;width:739px;height:65px;background:var(--yellow);display:flex;justify-content:space-around;padding:0 70px}
.contact-band div{display:flex;flex-direction:column;align-items:center;justify-content:center;gap:4px;font-size:12px;font-weight:700;color:var(--navy)}

/* footer */
.site-footer{position:absolute;left:0;top:1000px;width:739px;height:170px;background:var(--navy);display:flex;padding:40px 40px 0 40px;color:#fff}
.site-footer ul{list-style:none;width:150px;font-size:7.5px;line-height:1.9}
.site-footer ul li::before{content:"\203A  ";color:var(--yellow)}
.follow{margin-left:auto;font-size:9px;font-weight:600}
.follow div{display:flex;gap:6px;margin-top:8px}
.follow span{width:22px;height:22px;background:var(--yellow);border-radius:3px;display:block}
.copyright{position:absolute;left:0;top:1170px;width:739px;height:30px;background:var(--navy-deep);color:#c8cde0;font-size:7.5px;text-align:center;line-height:30px}
</style>
</head>
<body>

<header class="site-header">
  <div class="top-strip"></div>
  <a class="brand" href="#"><span class="brand-dot"></span><span class="brand-name">GTA</span></a>
  <div class="tagline-bar">Serving the Automotive Repair Industry Since 1947</div>
  <div class="search">Search</div>
  <div class="socials"><span></span><span></span><span></span></div>
  <nav class="main-nav">
    <ul>
      <li>Home</li><li>About</li><li>Membership</li><li>GTA Members</li><li>GTA Events</li><li>TechDocs Library</li><li>Market Research</li><li>Contact</li>
    </ul>
  </nav>
</header>

<section class="hero" role="img" aria-label="Photo of a mechanic in blue overalls holding a large wrench">
  <form class="login">
    <h2>The Garage Tools Alliance</h2>
    <div class="field"><label>Email</label><span></span></div>
    <div class="field"><label>Password</label><span></span></div>
    <div class="login-actions"><a href="#">Forgot Password</a><span class="btn-login">Login</span></div>
  </form>
  <div class="dots"><span></span><span></span><span></span><span></span></div>
</section>

<section class="intro">
  <p class="intro-lead">LOREM IPSUM IS SIMPLY DUMMY TEXT OF THE PRINTING HE STANDARD CHUNK OF LOREM</p>
  <div class="intro-body">
    <h2>THE GARAGE TOOLS ALLIANCE</h2>
    <p>Contrary to popular belief, Lorem Ipsum is not simply random text. It has roots in a piece of classical Latin literature from 45 BC, making it over 2000 years old. A Latin professor looked up one of the more obscure Latin words, consectetur, from a Lorem Ipsum passage, and going through the cites of the word in classical literature, discovered the undoubtable source of this text.</p>
  </div>
</section>

<section class="events">
  <h2>Upcomming Events</h2>
  <div class="event-grid">
    <article class="event">
      <span class="event-icon"><svg width="16" height="16" viewBox="0 0 16 16"><rect x="1.5" y="3" width="13" height="11.5" rx="1" fill="none" stroke="#1d2a5c" stroke-width="1.5"/><line x1="1.5" y1="6.5" x2="14.5" y2="6.5" stroke="#1d2a5c" stroke-width="1.5"/><line x1="5" y1="1" x2="5" y2="4" stroke="#1d2a5c" stroke-width="1.5"/><line x1="11" y1="1" x2="11" y2="4" stroke="#1d2a5c" stroke-width="1.5"/></svg></span>
      <div><h3>Contrary to popular belief, Lorem Ipsum</h3><p>The standard chunk of Lorem Ipsum used since the 1500s is reproduced below for those interested. Sections 1.10.32 and 1.10.33 are also shown.</p></div>
    </article>
    <article class="event">
      <span class="event-icon"><svg width="16" height="16" viewBox="0 0 16 16"><rect x="1.5" y="3" width="13" height="11.5" rx="1" fill="none" stroke="#1d2a5c" stroke-width="1.5"/><line x1="1.5" y1="6.5" x2="14.5" y2="6.5" stroke="#1d2a5c" stroke-width="1.5"/><line x1="5" y1="1" x2="5" y2="4" stroke="#1d2a5c" stroke-width="1.5"/><line x1="11" y1="1" x2="11" y2="4" stroke="#1d2a5c" stroke-width="1.5"/></svg></span>
      <div><h3>Contrary to popular belief, Lorem Ipsum</h3><p>The standard chunk of Lorem Ipsum used since the 1500s is reproduced below for those interested. Sections 1.10.32 and 1.10.33 are also shown.</p></div>
    </article>
    <article class="event">
      <span class="event-icon"><svg width="16" height="16" viewBox="0 0 16 16"><rect x="1.5" y="3" width="13" height="11.5" rx="1" fill="none" stroke="#1d2a5c" stroke-width="1.5"/><line x1="1.5" y1="6.5" x2="14.5" y2="6.5" stroke="#1d2a5c" stroke-width="1.5"/><line x1="5" y1="1" x2="5" y2="4" stroke="#1d2a5c" stroke-width="1.5"/><line x1="11" y1="1" x2="11" y2="4" stroke="#1d2a5c" stroke-width="1.5"/></svg></span>
      <div><h3>Contrary to popular belief, Lorem Ipsum</h3><p>The standard chunk of Lorem Ipsum used since the 1500s is reproduced below for those interested. Sections 1.10.32 and 1.10.33 are also shown.</p></div>
    </article>
    <article class="event">
      <span class="event-icon"><svg width="16" height="16" viewBox="0 0 16 16"><rect x="1.5" y="3" width="13" height="11.5" rx="1" fill="none" stroke="#1d2a5c" stroke-width="1.5"/><line x1="1.5" y1="6.5" x2="14.5" y2="6.5" stroke="#1d2a5c" stroke-width="1.5"/><line x1="5" y1="1" x2="5" y2="4" stroke="#1d2a5c" stroke-width="1.5"/><line x1="11" y1="1" x2="11" y2="4" stroke="#1d2a5c" stroke-width="1.5"/></svg></span>
      <div><h3>Contrary to popular belief, Lorem Ipsum</h3><p>The standard chunk of Lorem Ipsum used since the 1500s is reproduced below for those interested. Sections 1.10.32 and 1.10.33 are also shown.</p></div>
    </article>
  </div>
</section>

<section class="panels">
  <div class="panel">
    <h2>Industry News</h2>
    <div class="panel-body">
      <div class="news-item"><strong>1. Lorem Ipsum is simply dummy text</strong>The standard chunk of Lorem Ipsum used since the 1500s is reproduced below for<br><em>29th January, 2015</em></div>
      <div class="news-item"><strong>2. Lorem Ipsum is simply dummy text</strong>The standard chunk of Lorem Ipsum used since the 1500s is reproduced below for<br><em>29th January, 2015</em></div>
    </div>
  </div>
  <div class="panel">
    <h2>Quick Links</h2>
    <div class="panel-body">
      <div class="quick-grid">
        <span>Lorem Ipsum</span><span>Lorem Ipsum</span>
        <span>Lorem Ipsum</span><span>Lorem Ipsum</span>
        <span>Lorem Ipsum</span><span>Lorem Ipsum</span>
        <span class="wide">Lorem Ipsum</span>
      </div>
    </div>
  </div>
  <div class="panel join">
    <h2>Join GTA</h2>
    <div class="panel-body">
      <strong>Lorem Ipsum is simply dummy text</strong> The standard chunk of Lorem Ipsum used since the 1500s is reproduced below for those interested. Sections 1.10.32 and 1.10.33 are also reproduced in their exact original form, with English versions.
      <br><span class="btn-join">Join Now</span>
    </div>
  </div>
</section>

<section class="contact-row">
  <span>018000-555-0142</span>
  <span>25 Lorem Ipsum Street, CA</span>
  <span>info@gta-example.com</span>
</section>

<section class="contact-band">
  <div><svg width="20" height="20" viewBox="0 0 20 20"><path d="M5 2l3 4-2 2c1 2.5 3.5 5 6 6l2-2 4 3-2 3C9 17 3 11 2 4z" fill="#1d2a5c"/></svg>Call Us</div>
  <div><svg width="20" height="20" viewBox="0 0 20 20"><path d="M10 1a6 6 0 0 0-6 6c0 5 6 12 6 12s6-7 6-12a6 6 0 0 0-6-6z" fill="#1d2a5c"/><circle cx="10" cy="7" r="2.3" fill="#f4c21a"/></svg>Contact Us</div>
  <div><svg width="22" height="20" viewBox="0 0 22 20"><rect x="1" y="4" width="20" height="13" rx="1" fill="#1d2a5c"/><path d="M1.5 4.5l9.5 7 9.5-7" fill="none" stroke="#f4c21a" stroke-width="1.5"/></svg>Email Us</div>
</section>

<footer class="site-footer">
  <ul><li>Important dolor sit</li><li>Lorem ipsum is simply</li><li>There are many variations</li></ul>
  <ul><li>There are many variations</li><li>Which don't look even</li><li>Contact</li><li>About</li><li>Blog</li></ul>
  <ul><li>Which don't look even</li><li>Lorem Ipsum dolor sit</li><li>Contact us</li><li>There are many variations</li></ul>
  <div class="follow">Follow Us On:<div><span></span><span></span><span></span></div></div>
</footer>
<div class="copyright">©2015 Garage Tools Alliance All Right Reserved</div>

</body>
</html>
```